依頼詳細
【必ず入れて頂きたい要素】
①「アルコールと天然由来成分のチカラで室内除菌」というキャッチコピー。
②画像を使用し、キャッチコピーのイメージを入居者様が勝手に抱くデザイン。
※キャッチコピーとデザインで勝負し、下記の補足説明は可能な限り文字数を少なく、小さくする。

【補足説明として入れて頂きたい要素】
①「消臭・除菌施工サービス」というサービス名称。
②アルコールと国産の天然ひのきと緑茶エキスを使用。
③「中和反応法で悪臭の原因成分を分解」という事を添付画像「中和反応法」
のように図で説明。
④「第三者機関で効果を検証」という文言。
※添付画像「室内空気衛生推進連盟」のマークを挿入。

⑤2つの会社情報を記入するスペースを確保
1つは自由に社名や電話番号を記載できるように空欄とする
スペースのタイトルは「サービス提供会社」

1つは弊社の下記情報を記載
タイトルは「技術提供会社」
添付画像「会社ロゴ」
住所:東京都港区芝浦4-17-6森田ビル5F
電話:03-5871-2943
Mail:info@kt-planwork.jp
記載項目
株式会社住環境企画工房/東京都港区芝浦4-17-6森田ビル5F
電話:03-5871-2943/Mail:info@kt-planwork.jp
サイズ
A4
ページ数
片面
希望イメージ
シンプル 複雑
単色 カラフル
暗い 明るい
日常 高級
遊び心 厳粛
未来的 伝統的
女性的 男性的
希望する色
緑系、青系、水色系
納品ファイル
• 高解像度JPG (.jpg)
• イラストレーター形式 (.ai)
• PNG形式 (.png)
補足説明
下記3種のファイルでの納品お願い致します。
Ai(アウトライン前とアウトライン後)
PDF
jpg
(全てトンボ有り・無し両方)

```html
<!DOCTYPE html>
<html lang="ja">
<head>
<meta charset="utf-8">
<title>消臭抗菌 施工サービス</title>
<link rel="stylesheet" href="https://fonts.googleapis.com/css2?family=Noto+Sans+JP:wght@400;500;700&family=Noto+Serif+JP:wght@500;700&display=swap">
<style>
:root{
  --blue:#2f8fd0;
  --blue-deep:#1c6fb0;
  --sky:#dff0fa;
  --sky-soft:#eef7fc;
  --green:#5aa83a;
  --green-deep:#3f8a2a;
  --orange:#f39a2b;
  --ink:#333a40;
  --grey:#6b747c;
  --white:#ffffff;
}
*{margin:0;padding:0;box-sizing:border-box}
html,body{width:846px;height:1200px;overflow:hidden;background:var(--white)}
body{font-family:"Noto Sans JP",sans-serif;color:var(--ink)}
.flyer{position:relative;width:846px;height:1200px;overflow:hidden;background:var(--white)}
.hero-photo{position:absolute;left:0;top:0;width:846px;height:1040px;
  background:radial-gradient(circle at 20% 30%,#ffffff 0,#f4fafd 30%,transparent 60%),
  linear-gradient(180deg,#f7fbfd 0%,#e6f2f9 45%,#d3e8f3 80%,#c9e2ef 100%)}
.hero-subject{position:absolute;left:150px;top:380px;width:420px;height:400px;border-radius:45% 45% 20% 20%;
  background:linear-gradient(180deg,rgba(60,90,120,.18),rgba(80,110,140,.28))}
.title{position:absolute;left:270px;top:52px;font-family:"Noto Serif JP",serif;font-weight:700;color:var(--blue);
  font-size:108px;line-height:112px;letter-spacing:36px}
.subtitle{position:absolute;left:276px;top:288px;font-family:"Noto Serif JP",serif;font-weight:500;color:var(--blue-deep);font-size:34px;letter-spacing:3px}
.badge{position:absolute;border-radius:50%;display:flex;align-items:center;justify-content:center;text-align:center;font-weight:700}
.badge-virus{left:146px;top:212px;width:94px;height:94px;background:rgba(255,255,255,.85);border:2px solid var(--blue);color:var(--blue);font-size:15px;line-height:1.35}
.badge-natural{left:582px;top:282px;width:122px;height:122px;background:var(--green);color:var(--white);font-size:15px;line-height:1.35}
.badge-natural b{font-size:21px;display:block}
.catch{position:absolute;left:548px;top:412px;font-family:"Noto Serif JP",serif;color:var(--ink);font-weight:500;font-size:26px;line-height:1.55}
.catch .big{display:block;font-size:40px;color:var(--blue-deep);font-weight:700;margin-top:4px}
.panels{position:absolute;left:52px;top:748px;width:746px;height:282px;display:flex;gap:14px}
.panel{background:rgba(255,255,255,.92);border-radius:4px;overflow:hidden}
.panel-method{width:500px}
.panel-verify{width:232px;padding:0 14px}
.panel-head{background:var(--blue);color:var(--white);font-weight:700;font-size:17px;padding:8px 14px}
.panel-verify .panel-head{background:none;color:var(--blue-deep);font-size:20px;padding:10px 0 6px;border-bottom:2px solid var(--blue)}
.method-lead{font-size:12.5px;line-height:1.6;padding:10px 16px 4px}
.method-lead em{font-style:normal;color:var(--blue-deep);font-weight:700}
.diagram{display:block;margin:0 auto}
.verify-text{font-size:11.5px;line-height:1.6;margin-top:10px;color:var(--grey)}
.seal{width:92px;height:92px;border-radius:50%;background:var(--sky);border:3px solid var(--blue);margin-top:12px}
.seal-note{position:absolute;font-size:10px;color:var(--grey);line-height:1.5}
.footer{position:absolute;left:52px;top:1052px;width:746px;display:flex;gap:30px}
.company{width:358px;font-size:12px;line-height:1.65}
.company-label{font-size:11px;color:var(--grey);margin-bottom:6px}
.company-name{display:flex;align-items:center;gap:10px;font-weight:700;font-size:18px;color:var(--blue-deep);margin-bottom:4px}
.company-name i{width:18px;height:18px;background:var(--blue);display:block}
.blank{border-left:1px solid #c8d3da;padding-left:24px}
</style>
</head>
<body>
<div class="flyer">
  <div class="hero-photo" role="img" aria-label="明るい窓辺の室内で床に座ってくつろぐ女性と、空中に漂う透明なシャボンの泡"></div>
  <div class="hero-subject" role="img" aria-label="白いトップスとデニムで床に座る女性のシルエット領域"></div>

  <h1 class="title">消臭<br>抗菌</h1>
  <p class="subtitle">施工サービス</p>

  <div class="badge badge-virus">ウイルス<br>対策にも!</div>
  <div class="badge badge-natural"><span>国産の天然<b>ひのき&amp;緑茶</b>エキス使用</span></div>

  <p class="catch">アルコールと<br>天然由来成分のチカラで<span class="big">室内除菌</span></p>

  <div class="panels">
    <section class="panel panel-method">
      <h2 class="panel-head">中和反応法で悪臭の原因成分を分解</h2>
      <p class="method-lead">悪臭の原因成分(<em>アンモニア・ピリジン・トリメチルアミン</em>)を<br>ニオイのない成分に変化させます。</p>
      <svg class="diagram" width="470" height="160" viewBox="0 0 470 160">
        <text x="90" y="18" font-size="12" text-anchor="middle" fill="#333a40">一般の芳香剤</text>
        <circle cx="90" cy="75" r="42" fill="#fde3c2"/>
        <circle cx="78" cy="68" r="14" fill="#f39a2b"/>
        <circle cx="104" cy="86" r="12" fill="#e57373"/>
        <text x="90" y="140" font-size="11" text-anchor="middle" fill="#e57373">香りの中に悪臭が残る</text>
        <line x1="185" y1="10" x2="185" y2="150" stroke="#c8d3da" stroke-dasharray="3 3"/>
        <text x="330" y="18" font-size="12" text-anchor="middle" fill="#333a40">天然植物エキス &amp; 緑茶抽出エキス</text>
        <circle cx="240" cy="70" r="22" fill="#e57373"/>
        <text x="240" y="74" font-size="11" text-anchor="middle" fill="#fff">悪臭</text>
        <text x="276" y="75" font-size="18" text-anchor="middle" fill="#2f8fd0">+</text>
        <circle cx="312" cy="70" r="22" fill="#5aa83a"/>
        <text x="312" y="74" font-size="11" text-anchor="middle" fill="#fff">エキス</text>
        <path d="M342 70h34m-8-7l8 7-8 7" stroke="#2f8fd0" stroke-width="3" fill="none"/>
        <circle cx="414" cy="70" r="30" fill="#dff0fa" stroke="#2f8fd0" stroke-width="2"/>
        <text x="414" y="74" font-size="11" text-anchor="middle" fill="#1c6fb0">無臭</text>
        <text x="330" y="140" font-size="11" text-anchor="middle" fill="#1c6fb0">ニオイのない成分に変化</text>
      </svg>
    </section>
    <section class="panel panel-verify">
      <h2 class="panel-head">第三者機関で効果を検証</h2>
      <p class="verify-text">室内空気衛生推進連盟にて第三者機関による消臭試験を行い、アンモニア等の悪臭成分への効果を確認しています。</p>
      <div class="seal" role="img" aria-label="認定マーク"></div>
      <p class="seal-note" style="left:658px;top:212px;width:130px">室内空気衛生推進連盟に<br>認定された製品です。</p>
    </section>
  </div>

  <footer class="footer">
    <div class="company">
      <p class="company-label">【技術提供会社】</p>
      <p class="company-name"><i></i>株式会社住環境企画工房</p>
      <p>東京都港区芝浦4-17-6森田ビル5F</p>
      <p>TEL 03-5871-2943</p>
      <p>Mail info@kt-planwork.jp</p>
    </div>
    <div class="company blank">
      <p class="company-label">【サービス提供会社】</p>
    </div>
  </footer>
</div>
</body>
</html>
```